Closing our Brindel Office

I currently have a three location eye care practice located in Spokane Valley, Airway Heights and Brindel Marketways. We are closing our Brindel location and hope to see these patients at our other practices.
Updates

I would like something that comes across as more friendly and appreciative... "Thank you for seeing us at our Brindel Marketway clinic. This location has now closed. We hope to continue to provide care for you at our Airway Heights or Spokane Valley locations. -Dr Tavo Rennick, Mila and Odette This will be on a postcard, so it needs to have space for address and stamp. Must have picture of the three of us on the front, and picture of both locations (wide view showing mural) on the back. (okay to include or leave out picture of me on back) Please include address with pictures: Spokane Valley Clinic- 48316 E Carrow Ln. Airway Heights Clinic - 3094 S Pimbury Rd. Also need to include Phone number : 509-418-2639, www.brightlenscare.com, and hello@brightlenscare.com.

Target Market(s)

Current Brindel patients

Font styles to use
Serif
Sans Serif

Requirements
Must have
• Photo of myself and two staff.
• Photo of Airway Heights and Valley office
• Photo with mural to left is my Airway office. Photo with mural to the right is Spokane Valley (Marlowe Exit)
• Phone # 509-418-2639. www.brightlenscare.com
Nice to have
• Front of card with photo of myself, Mila (darker hair on left) and Odete (longer hair on right)
• Back of card with images of both other clinics and small photo of myself

```html
<!DOCTYPE html>
<html lang="en">
<head>
<meta charset="utf-8">
<title>Brindel Closing Postcard</title>
<link href="https://fonts.googleapis.com/css2?family=Ubuntu:wght@400;500&display=swap" rel="stylesheet">
<style>
  :root {
    --page: #ffffff;
    --navy-light: #3a5d8f;
    --navy: #2c4b7a;
    --navy-deep: #1d3459;
    --band-grey: #707c8c;
    --panel-white: #fdfdfd;
    --rule: #3a3a3a;
    --quote-grey: #a8b0bc;
    --ink-dark: #2a3140;
    --ink-light: #ffffff;
    --brand-blue: #1f66b3;
    --brand-navy: #1c3a6e;
    --mural-light: #dedad6;
    --mural-mid: #a9a6a4;
    --office-wall: #7d8088;
    --office-dark: #3b3d44;
    --desk-white: #e9eaec;
    --team-bg: #e4dfdd;
    --team-hair: #6b5244;
    --team-skin: #d9ac95;
    --team-shirt: #f2f2f4;
  }
  * { box-sizing: border-box; margin: 0; padding: 0; }
  html, body {
    width: 884px; height: 1200px; overflow: hidden;
    background: var(--page);
    font-family: "Ubuntu", sans-serif;
  }
  .canvas { position: relative; width: 884px; height: 1200px; }

  .postcard {
    position: absolute;
    background: linear-gradient(180deg, var(--navy-light) 0%, var(--navy) 55%, var(--navy-light) 100%);
    box-shadow: 0 4px 16px rgba(0,0,0,0.45);
    overflow: hidden;
  }
  .postcard--back { left: 64px; top: 50px; width: 755px; height: 534px; }
  .postcard--front { left: 64px; top: 600px; width: 759px; height: 538px; }

  .abs { position: absolute; }

  /* back side */
  .band-grey { background: var(--band-grey); }
  .band-deep { background: var(--navy-deep); }
  .caption {
    color: var(--ink-light); font-size: 14px; text-align: center;
    display: flex; align-items: center; justify-content: center;
    letter-spacing: 0.2px;
  }
  .clinic-photo--airway {
    background:
      linear-gradient(180deg, rgba(0,0,0,0) 0%, rgba(0,0,0,0) 72%, rgba(40,40,46,0.55) 80%, rgba(233,234,236,0.85) 90%, rgba(233,234,236,0.9) 100%),
      linear-gradient(90deg, var(--mural-light) 0%, var(--mural-mid) 18%, var(--mural-light) 32%, var(--office-wall) 48%, #9a9ca3 62%, #c2c4c8 72%, var(--office-wall) 86%, var(--office-dark) 100%);
  }
  .clinic-photo--valley {
    background:
      linear-gradient(180deg, rgba(0,0,0,0) 0%, rgba(0,0,0,0) 74%, rgba(30,30,34,0.6) 86%, rgba(50,50,56,0.7) 100%),
      linear-gradient(90deg, var(--office-dark) 0%, #b9babd 12%, #9fa1a6 30%, var(--office-wall) 52%, #6e7178 62%, var(--mural-light) 68%, var(--mural-mid) 84%, var(--mural-light) 100%);
  }
  .contact { color: var(--ink-light); font-size: 14px; line-height: 17px; letter-spacing: 0.2px; }
  .contact--right { text-align: right; }

  .address-panel {
    left: 388px; top: 14px; width: 350px; height: 507px;
    background: var(--panel-white); border-radius: 4px;
  }
  .stamp-box { left: 219px; top: 28px; width: 114px; height: 113px; border: 1px solid var(--rule); }
  .address-line { left: 18px; width: 315px; height: 1px; background: var(--rule); }
  .brand {
    left: 0; width: 350px; top: 438px;
    display: flex; align-items: center; justify-content: center; gap: 8px;
  }
  .brand__mark { width: 14px; height: 14px; border-radius: 50%; background: var(--brand-blue); }
  .brand__name { font-size: 18px; font-weight: 500; color: var(--brand-navy); letter-spacing: 0.3px; }

  /* front side */
  .site-url { left: 0; width: 759px; top: 43px; text-align: center; color: var(--ink-light); font-size: 17px; }
  .team-photo {
    left: 100px; top: 98px; width: 562px; height: 264px; border-radius: 4px;
    background:
      linear-gradient(180deg, rgba(0,0,0,0) 0%, rgba(0,0,0,0) 30%, rgba(0,0,0,0.05) 100%),
      linear-gradient(90deg,
        var(--team-bg) 0%, var(--team-bg) 6%,
        var(--team-hair) 14%, var(--team-skin) 22%, var(--team-skin) 30%, var(--team-hair) 40%,
        var(--team-shirt) 47%, #e8e4e6 58%,
        var(--team-hair) 64%, var(--team-skin) 72%, var(--team-skin) 82%, var(--team-hair) 92%,
        var(--team-bg) 100%);
    box-shadow: 0 2px 6px rgba(0,0,0,0.35);
  }
  .message-band { left: 0; top: 372px; width: 759px; height: 133px; background: var(--navy-deep); }
  .message-box {
    left: 100px; top: 384px; width: 562px; height: 108px; border-radius: 4px;
    background: var(--quote-grey); color: var(--ink-dark); text-align: center;
    padding-top: 12px;
  }
  .message-box__text { font-size: 16px; line-height: 19.5px; padding: 0 22px; }
  .message-box__sign { font-size: 20px; margin-top: 7px; letter-spacing: 0.6px; }
</style>
</head>
<body>
<div class="canvas">

  <section class="postcard postcard--back">
    <div class="abs band-grey" style="left:0;top:74px;width:755px;height:24px;"></div>
    <div class="abs caption" style="left:0;top:74px;width:388px;height:24px;">Airway Heights Clinic - 3094 S Pimbury Rd</div>
    <div class="abs band-grey" style="left:738px;top:98px;width:17px;height:72px;"></div>
    <div class="abs band-deep" style="left:0;top:170px;width:755px;height:121px;"></div>
    <div class="abs clinic-photo--airway" style="left:8px;top:98px;width:380px;height:146px;" role="img" aria-label="Airway Heights clinic reception with eye chart mural on the left"></div>
    <div class="abs clinic-photo--valley" style="left:0;top:291px;width:388px;height:145px;" role="img" aria-label="Spokane Valley clinic reception with eye chart mural on the right"></div>
    <div class="abs band-grey" style="left:0;top:408px;width:755px;height:52px;"></div>
    <div class="abs caption" style="left:0;top:436px;width:388px;height:24px;">Spokane Valley Clinic- 48316 E Carrow Ln.</div>
    <div class="abs contact" style="left:19px;top:475px;">Phone number :<br>509-418-2639</div>
    <div class="abs contact contact--right" style="left:160px;top:475px;width:214px;">hello@brightlenscare.com<br>www.brightlenscare.com</div>

    <div class="abs address-panel">
      <div class="abs stamp-box"></div>
      <div class="abs address-line" style="top:196px;"></div>
      <div class="abs address-line" style="top:252px;"></div>
      <div class="abs address-line" style="top:318px;"></div>
      <div class="abs brand">
        <span class="brand__mark"></span>
        <span class="brand__name">BRIGHTLENS VISION</span>
      </div>
    </div>
  </section>

  <section class="postcard postcard--front">
    <p class="abs site-url">www.brightlenscare.com</p>
    <div class="abs team-photo" role="img" aria-label="Photo of Dr Tavo Rennick with Mila and Odette in front of the eye chart mural"></div>
    <div class="abs message-band"></div>
    <div class="abs message-box">
      <p class="message-box__text">"Thank you for seeing us at our Brindel Marketway clinic. This location has now closed. We hope to continue to provide care for you at our Airway Heights or Spokane Valley locations.</p>
      <p class="message-box__sign">- Dr Tavo Rennick ,Mila and Odette -</p>
    </div>
  </section>

</div>
</body>
</html>
```